Require stationery design: letter head and update existing business card

clean, simple, minamilistic, los of negative space, black or white. casual, but passionate, informative and knowledgable , no fuss, don to earth.

logo newly created and supplied As AI files in breif. . TO CONFIRM THE FINAL LOGO IS THE VERSION WITH THE GRAPHIC / PICTURE INCLUDED. we now need to update our business card design, take old logo out and replace with new logo, raw business files supplied in brief.
For business card I need proofs with white, black and ligjt timber / rustic cookie.

Target Market(s)

women, house wives, business men, hospitality, higher socio economic, commercial residential, niche market.

Industry/Entity Type

Business

Number of Pages Required

3 page

Font styles to use
Sans Serif

Colors
ffffff
3277b5
0355a3
faa54b
f68e4e

Requirements
Must have
• proofs for business card design to be provided on white, black, timber / cardboard background. logo and business to be supplied in all usable formats and files.
• Letter head to be A4 against white background. Supplier in WORDDOC or send header and footer images as JPEG so I can insert into word template
• suitable quote, invoice, receipt template for emailed pdf's
Nice to have
• stylised touch. finesse. sophistication. we are competed in this kind of market.
• use the colour featured in the screen shot file of a random logo
Should not have
• clutter. be crowded. more than 2 fonts.

```html
<!DOCTYPE html>
<html lang="en">
<head>
<meta charset="utf-8">
<title>Timberline &amp; Grain Co. — Letterhead</title>
<link rel="stylesheet" href="https://fonts.googleapis.com/css2?family=Open+Sans:ital,wght@0,400;0,600;0,700;1,400&display=swap">
<style>
  :root {
    --backdrop: #e9b77a;
    --paper: #ffffff;
    --paper-cream: #fdfbe9;
    --navy: #1f4159;
    --amber: #faa54b;
    --amber-deep: #f68e4e;
    --ink: #3a3a3a;
    --ink-soft: #6b6b6b;
    --mist: #d9dcdf;
  }
  * { box-sizing: border-box; margin: 0; padding: 0; }
  html, body { width: 1200px; height: 784px; overflow: hidden; }
  body {
    background: var(--backdrop);
    font-family: "Open Sans", Arial, sans-serif;
    color: var(--ink);
    position: relative;
  }
  .letterhead {
    position: absolute;
    left: 338px; top: 22px;
    width: 523px; height: 740px;
    background: linear-gradient(180deg, var(--paper) 0%, var(--paper) 55%, var(--paper-cream) 100%);
    box-shadow: 0 6px 18px rgba(120, 70, 20, 0.25);
    overflow: hidden;
  }
  /* corner accents */
  .accent { position: absolute; }
  .accent--top-navy   { left: 0; top: 0; width: 28px; height: 5px; background: var(--navy); }
  .accent--top-amber  { left: 0; top: 5px; width: 5px; height: 24px; background: var(--amber); }
  .accent--side-navy  { right: 0; top: 0; width: 5px; height: 30px; background: var(--navy); }
  .accent--side-amber { right: 0; top: 30px; width: 5px; height: 26px; background: var(--amber); }
  .accent--foot-amber { left: 0; bottom: 0; width: 5px; height: 22px; background: var(--amber); }
  .accent--foot-amber-h { left: 0; bottom: 0; width: 90px; height: 5px; background: var(--amber); }
  .accent--foot-navy  { left: 100px; bottom: 0; right: 0; height: 6px; background: var(--navy); }
  .accent--foot-amber-r { right: 0; bottom: 0; width: 5px; height: 22px; background: var(--amber-deep); }

  .brand {
    position: absolute; left: 40px; top: 30px;
    text-align: left;
  }
  .brand__web {
    font-size: 7px; letter-spacing: 2.4px; color: var(--navy); font-weight: 600;
    text-transform: uppercase;
  }
  .brand__name {
    display: flex; align-items: center; gap: 6px;
    margin-top: 4px;
    font-size: 17px; font-weight: 700; color: var(--amber);
  }
  .brand__dot { width: 9px; height: 9px; border-radius: 50%; background: var(--amber); }
  .brand__tagline {
    margin-top: 3px; font-size: 6px; letter-spacing: 2.6px; color: var(--amber-deep);
    text-transform: uppercase; font-weight: 600;
  }

  .contact {
    position: absolute; right: 30px; top: 40px; width: 150px;
    font-size: 7px; line-height: 1.55; color: var(--ink-soft);
  }
  .contact__address { font-weight: 700; color: var(--ink); margin-bottom: 4px; }
  .contact__row { display: flex; align-items: center; gap: 5px; }
  .contact__bullet { width: 5px; height: 5px; border-radius: 50%; background: var(--amber); flex: none; }

  .letter {
    position: absolute; left: 70px; top: 120px; width: 400px;
  }
  .letter__salutation { font-size: 14px; font-weight: 400; color: var(--ink); margin-bottom: 14px; }
  .letter__body p {
    font-size: 9.5px; line-height: 1.65; color: var(--ink-soft); margin-bottom: 10px;
  }
  .signature {
    width: 70px; height: 40px; margin-top: 18px;
    background: linear-gradient(90deg, #e8e8e8, #f4f4f4);
    border-radius: 4px;
  }

  .landscape {
    position: absolute; left: 150px; right: 40px; bottom: 40px; height: 240px;
    background: radial-gradient(ellipse at 60% 70%, var(--mist) 0%, rgba(217,220,223,0.4) 45%, rgba(255,255,255,0) 75%);
  }
</style>
</head>
<body>
  <article class="letterhead">
    <span class="accent accent--top-navy"></span>
    <span class="accent accent--top-amber"></span>
    <span class="accent accent--side-navy"></span>
    <span class="accent accent--side-amber"></span>
    <span class="accent accent--foot-amber"></span>
    <span class="accent accent--foot-amber-h"></span>
    <span class="accent accent--foot-navy"></span>
    <span class="accent accent--foot-amber-r"></span>

    <header class="brand">
      <div class="brand__web">www.timberlinegrain.co.nz</div>
      <div class="brand__name"><span class="brand__dot"></span>Timberline &amp; Grain Co.</div>
      <div class="brand__tagline">The Slab Furniture Company</div>
    </header>

    <address class="contact" style="font-style:normal">
      <div class="contact__address">Suite 0, 000 Harbour Rd.<br>KELBURN, NZ 0000</div>
      <div class="contact__row"><span class="contact__bullet"></span>(00) 000 0000</div>
      <div class="contact__row"><span class="contact__bullet"></span>0000 000 000</div>
      <div class="contact__row"><span class="contact__bullet"></span>info@timberlinegrain.co.nz</div>
      <div class="contact__row"><span class="contact__bullet"></span>www.timberlinegrain.co.nz</div>
    </address>

    <section class="letter">
      <h1 class="letter__salutation">Dear Mr. Solicitor,</h1>
      <div class="letter__body">
        <p>Lorem ipsum dolor sit amet, consectetur adipiscing elit. Vestibulum nec nunc sollicitudin, dictum ligula vitae, accumsan felis. Donec at quam felis. Pellentesque feugiat condimentum adipiscing. Maecenas sit amet neque ligula. Suspendisse ut libero in justo ullamcorper porttitor et vel orci. In consequat nibh in lacinia facilisis. Interdum et malesuada fames ac ante ipsum primis in faucibus. Cras adipiscing turpis lacus, eu faucibus nibh laoreet vel. Etiam pellentesque, massa eu sodales interdum, mi nisi sagittis sem, sit amet feugiat turpis erat ac arcu. Proin at tincidunt nulla, sed feugiat massa. Maecenas suscipit purus nec orci rutrum, non auctor eros vulputate. Ut nec erat mollis, placerat risus venenatis, pharetra quam. Mauris hendrerit interdum ante, nec molestie ipsum faucibus eu.</p>
        <p>Nulla nec risus non quam mollis volutpat. Suspendisse sit amet dignissim purus. Sed fringilla ipsum eu ullamcorper posuere. In odio odio, tempor eu dictum a, pulvinar eu eros. Sed suscipit id risus a rhoncus. Mauris mollis dictum libero, vel lacinia sapien ullamcorper quis. Ut nec erat mollis, placerat risus venenatis, pharetra quam. Mauris hendrerit interdum ante, nec molestie ipsum faucibus eu. Etiam ultricies, sapien quis blandit ullamcorper, diam diam mollis urna, sed tempor diam nulla ut odio. Cras sollicitudin semper convallis. Sed suscipit id risus a rhoncus.</p>
      </div>
      <div class="signature" role="img" aria-label="Handwritten signature of the sender"></div>
    </section>

    <div class="landscape" role="img" aria-label="Faint grey line illustration of rolling hills and trees"></div>
  </article>
</body>
</html>
```